Website for Private Psychologist

DO NOT CONTACT ME PRIVATELY

I am a Psychologist offering psychotherapy for individuals and couples, and clinical consultation and training and education for mental and medical health professionals and agencies.

I need a redesign of my website

5 Pages (content is attached for each page)
Home
Jungian Psychotherapy
Clinical Consultation & Professional Development
Curriculum Vitae & Publications
Practice Policies and Forms

Designs can be based on these style websites
https://lqmindcare.info; https://pdtarn.org/; https://dorabellcroftcounselling.com/

Design Concepts
Minimalist Layout: Clean and uncluttered layout with generous white space, allowing the content and visuals to stand out'

Keep a linear, uncluttered, professional design.

Please use only royalty free images and google fonts. Please provide links to any stock images used to verify license.

Target Market(s)

private individual or couples seeking psychotherapy

Industry/Entity Type

Psychotherapy

Number of Pages Required

5+ page

Requirements
Should not have
• No search feature

```html
<!DOCTYPE html>
<html lang="en">
<head>
<meta charset="utf-8">
<title>Elliot Marchetti, Psy.D.</title>
<link rel="stylesheet" href="https://fonts.googleapis.com/css2?family=Oswald:wght@500&family=Noto+Serif:wght@400;700&family=Source+Sans+3:wght@400;600;700&display=swap">
<style>
:root{
  --green:#1f8b50;
  --ink:#111;
  --grey:#555;
  --rule:#d8d8d8;
  --black:#000;
  --white:#fff;
}
*{margin:0;padding:0;box-sizing:border-box}
html,body{width:1200px;height:2904px;overflow:hidden;background:var(--white)}
body{position:relative;font-family:"Source Sans 3",sans-serif;color:var(--ink)}
.abs{position:absolute}
.topbar{left:0;top:0;width:1200px;height:3px;background:var(--green)}
.site-title{left:0;top:22px;width:1200px;text-align:center;font-family:"Oswald",sans-serif;font-weight:500;font-size:29px;letter-spacing:.3px}
.nav-rule{left:98px;top:82px;width:1004px;height:44px;border-top:1px solid var(--rule);border-bottom:1px solid var(--rule)}
.nav{left:95px;top:82px;width:1011px;height:44px;display:flex;align-items:center;justify-content:space-between;font-family:"Noto Serif",serif;font-size:13px;white-space:nowrap}
.nav a{flex:none;color:var(--ink);text-decoration:none;padding:0 14px;border-left:1px solid var(--green);line-height:20px}
.nav a:first-child{border-left:none;padding-left:0}
.nav a:last-child{padding-right:0}
.hero{left:98px;top:148px;width:1004px;height:501px;border-radius:34px;overflow:hidden;background:linear-gradient(90deg,#25935a 0%,#2f9862 38%,#8a8e86 62%,#6f6f78 82%,#8e8a8c 100%)}
.hero-text{left:49px;top:114px;color:var(--white);font-family:"Noto Serif",serif}
.hero-text .pre{font-size:36px;line-height:44px}
.hero-text h1{font-size:37px;font-weight:700;line-height:50px;margin-left:3px;letter-spacing:.5px;white-space:nowrap}
.hero-text p{font-size:14.5px;line-height:23px;width:440px;margin:16px 0 0 4px}
.btn{display:inline-flex;align-items:center;justify-content:center;border-radius:30px;text-decoration:none}
.btn-hero{margin:19px 0 0 6px;width:211px;height:45px;background:var(--white);color:var(--green);font-size:17px;font-family:"Noto Serif",serif}
.sec-title{font-family:"Noto Serif",serif;font-weight:700;letter-spacing:1px}
.spec-title{left:0;top:738px;width:1200px;text-align:center;font-size:37px}
.rule{height:2px;background:var(--green)}
.card{top:846px;width:318px;text-align:center}
.card .ph{height:223px;border-radius:14px;background:linear-gradient(160deg,#cfc6b6,#8a6a4a 55%,#3b2f28)}
.card h3{font-family:"Noto Serif",serif;font-weight:700;font-size:24px;color:var(--green);margin-top:20px;letter-spacing:.4px}
.card p{font-size:16px;line-height:22px;color:var(--grey);margin:10px auto 0;width:290px}
.band{left:0;top:1284px;width:1200px;height:526px;background:var(--green);overflow:hidden}
.band h2{position:absolute;left:100px;top:48px;color:var(--white);font-size:38px;line-height:49px;white-space:nowrap}
.band .rule{position:absolute;left:104px;top:152px;width:110px;background:var(--white)}
.band p{position:absolute;left:100px;top:172px;width:460px;color:var(--white);font-size:18px;line-height:31px}
.btn-band{position:absolute;left:99px;top:389px;width:205px;height:60px;background:var(--white);color:var(--green);font-size:23px;font-weight:700}
.band svg{position:absolute;left:0;top:0}
.about-ph{left:98px;top:1935px;width:458px;height:411px;border-radius:30px;background:linear-gradient(180deg,#d9d5cc 0%,#b8aa90 45%,#3d3a38 80%,#272a33 100%)}
.about h2{position:absolute;left:620px;top:1950px;font-size:37px;white-space:nowrap}
.about .rule{position:absolute;left:620px;top:2008px;width:113px}
.about p{position:absolute;left:621px;top:2031px;width:480px;font-family:"Noto Serif",serif;font-size:16.5px;line-height:26.7px;color:var(--grey)}
.btn-about{position:absolute;left:622px;top:2251px;width:206px;height:61px;background:var(--green);color:var(--white);font-size:23px;font-weight:700}
.footer{left:0;top:2436px;width:1200px;height:468px;background:var(--black);color:var(--white)}
.footer .name{position:absolute;left:0;top:52px;width:1200px;text-align:center;font-family:"Oswald",sans-serif;font-weight:500;font-size:57px}
.socials{position:absolute;left:496px;top:177px;display:flex;gap:34px}
.socials span{width:14px;height:14px;border-radius:50%;background:var(--white)}
.contact{position:absolute;top:252px;display:flex;align-items:center;gap:12px;white-space:nowrap}
.contact svg{flex:none}
.contact .lbl{font-size:13.5px;font-weight:700;color:var(--green);letter-spacing:.2px}
.contact .val{font-family:"Noto Serif",serif;font-size:18px;line-height:22px}
.footer .line{position:absolute;left:170px;top:351px;width:871px;height:1px;background:var(--green)}
.copy{position:absolute;left:0;top:380px;width:1200px;text-align:center;font-size:17px}
</style>
</head>
<body>
<div class="abs topbar"></div>
<div class="abs site-title">Elliot Marchetti, Psy.D.</div>
<div class="abs nav-rule"></div>
<nav class="abs nav">
  <a href="#">Home</a><a href="#">Jungian Psychotherapy</a><a href="#">Clinical Consultation &amp; Professional Development</a><a href="#">Curriculum Vitae &amp; Publications</a><a href="#">Practice Policies and Forms</a>
</nav>

<section class="abs hero" role="img" aria-label="Photo of a therapy session: a client on a green sofa speaking with a therapist">
  <div class="abs hero-text">
    <div class="pre">Welcome to</div>
    <h1>Elliot Marchetti, Psy.D</h1>
    <p>I am a Psychologist offering psychotherapy for individuals and couples, and clinical consultation and training and education for mental and medical health professionals and agencies.</p>
    <a class="btn btn-hero" href="#">Book a Consultation</a>
  </div>
</section>

<h2 class="abs sec-title spec-title">SPECIALIZATIONS</h2>
<div class="abs rule" style="left:561px;top:795px;width:78px"></div>

<div class="abs card" style="left:98px"><div class="ph" role="img" aria-label="Office photo with desk and bookshelf"></div><h3>Nemo enim ipsam</h3><p>Lorem ipsum dolor sit amet, consectetur adipiscing elit, sed do eiusmod tempor incididunt ut labore et dolore magna</p></div>
<div class="abs card" style="left:440px"><div class="ph" role="img" aria-label="Office photo with window, plants and armchair"></div><h3>Nemo enim ipsam</h3><p>Lorem ipsum dolor sit amet, consectetur adipiscing elit, sed do eiusmod tempor incididunt ut labore et dolore magna</p></div>
<div class="abs card" style="left:783px"><div class="ph" role="img" aria-label="Office photo with cabinet, bench and framed picture" style="background:linear-gradient(160deg,#e4e1da,#c9c2b4 55%,#5a4634)"></div><h3>Nemo enim ipsam</h3><p>Lorem ipsum dolor sit amet, consectetur adipiscing elit, sed do eiusmod tempor incididunt ut labore et dolore magna</p></div>

<section class="abs band">
  <svg width="1200" height="526" viewBox="0 0 1200 526">
    <defs><linearGradient id="portraitTone" x1="0" y1="0" x2="1" y2="1"><stop offset="0" stop-color="#8a7556"/><stop offset=".5" stop-color="#b0845e"/><stop offset="1" stop-color="#3f3a2c"/></linearGradient></defs>
    <circle cx="857" cy="264" r="266" fill="#000"/>
    <rect x="857" y="0" width="343" height="526" fill="url(#portraitTone)"/>
    <circle cx="866" cy="264" r="262" fill="url(#portraitTone)" role="img" aria-label="Portrait photo of the psychologist"/>
  </svg>
  <h2 class="sec-title">JUNGIAN PSYCHOTHERAPY<br>&amp; CONSULTATION</h2>
  <div class="rule"></div>
  <p>I am a California Licensed Psychologist with an office in the San Francisco Financial District offering psychotherapy for individuals and couples, and clinical consultation and training and education for mental and medical health professionals and agencies. All appointments are currently available via telehealth.</p>
  <a class="btn btn-band" href="#">Read More</a>
</section>

<div class="abs about-ph" role="img" aria-label="Photo of two armchairs beside a lamp in the consulting room"></div>
<section class="about">
  <h2 class="sec-title">JUNGIAN PSYCHOTHERAPY</h2>
  <div class="rule"></div>
  <p>I practice depth-oriented psychotherapy and tailor my approach to the individual or couple seeking treatment.&nbsp; I have experience treating a range of psychological issues including depression, anxiety, and relationship and job dissatisfaction as well as life transition issues such as college and graduate school stress, pre-marital counseling, and issues related to identity and sexuality.</p>
  <a class="btn btn-about" href="#">Read More</a>
</section>

<footer class="abs footer">
  <div class="name">Elliot Marchetti, Psy.D.</div>
  <div class="socials"><span></span><span></span><span></span><span></span><span></span></div>
  <div class="contact" style="left:173px">
    <svg width="40" height="40" viewBox="0 0 40 40"><circle cx="20" cy="20" r="19" fill="none" stroke="#fff" stroke-width="1"/><rect x="13" y="14.5" width="14" height="11" rx="1.5" fill="none" stroke="#fff" stroke-width="1.6"/><path d="M13.5 15.5l6.5 5 6.5-5" fill="none" stroke="#fff" stroke-width="1.6"/></svg>
    <div><div class="lbl">EMAIL</div><div class="val">emarchetti@quietmail.com</div></div>
  </div>
  <div class="contact" style="left:505px;top:256px">
    <svg width="40" height="40" viewBox="0 0 40 40"><circle cx="20" cy="20" r="19" fill="none" stroke="#fff" stroke-width="1"/><path d="M20 28c-4-5-5.5-7.5-5.5-10a5.5 5.5 0 0 1 11 0c0 2.5-1.5 5-5.5 10z" fill="#fff"/><circle cx="20" cy="18" r="2" fill="#000"/></svg>
    <div><div class="lbl">OUR LOCATION</div><div class="val">Harborview Analytic Institute.</div></div>
  </div>
  <div class="contact" style="left:864px">
    <svg width="40" height="40" viewBox="0 0 40 40"><circle cx="20" cy="20" r="19" fill="none" stroke="#fff" stroke-width="1"/><path d="M15 13.5l3 .2 1.3 3.3-2 1.4a10 10 0 0 0 4.3 4.3l1.4-2 3.3 1.3.2 3a2 2 0 0 1-2 1.5A12.5 12.5 0 0 1 13.5 15.5a2 2 0 0 1 1.5-2z" fill="#fff"/></svg>
    <div><div class="lbl">PHONE NUMBER</div><div class="val">(415) 555-0182</div></div>
  </div>
  <div class="line"></div>
  <div class="copy">© Copyrights 2023 Elliot Marchetti, Psy.D. |&nbsp; All Rights Reserved</div>
</footer>
</body>
</html>
```